TRUCK WASH OUTDOOR DRIVE THROUGH MENU CONTEST

WE NEED A DRIVE THROUGH MENU WITH OUR SERVICES AND PRICES. I HAVE ATTACHED A FEW EXAMPLES THAT I STARTED.

I WANT THIS TO BE EYE CATCHING WITH BRIGHT COLORS

Target Market(s)

TRUCK WASH AND DETAIL SHOP, TRANSPORTATION.

Requirements
Must have
• INCORPORATE MY LOGO INTO THE SIGN.
• FINAL PROJECT MUST BE IN .AI FORMAT.
• COMPANY COLORS ARE RED AND BLUE

```html
<!DOCTYPE html>
<html lang="en">
<head>
<meta charset="utf-8">
<title>Truck Wash Drive-Through Menu</title>
<link rel="stylesheet" href="https://fonts.googleapis.com/css2?family=Exo+2:ital,wght@1,900&family=Fira+Sans+Condensed:wght@600&family=Comfortaa:wght@700&display=swap">
<style>
  :root {
    --sky: #5fb6ea;
    --deep: #1d6fc0;
    --red: #ec1c24;
    --orange: #f7941d;
    --yellow: #f4ea2c;
    --green: #3aaa49;
    --green-dark: #0b5a22;
    --blue: #1f6fb8;
    --white: #ffffff;
  }
  * { margin: 0; padding: 0; box-sizing: border-box; }
  html, body { width: 1200px; height: 1200px; overflow: hidden; }
  .menu { position: relative; width: 1200px; height: 1200px; overflow: hidden; }
  .backdrop {
    position: absolute; inset: 0;
    background: radial-gradient(circle at 30% 20%, #9fd8f6 0%, var(--sky) 35%, var(--deep) 80%, #1a5ea8 100%);
  }
  .tier-title, .tier-details, .tier-price { position: absolute; }
  .tier-title {
    left: 0; border-radius: 0 60px 60px 0;
    display: flex; align-items: center;
    font-family: "Exo 2", sans-serif; font-style: italic; font-weight: 900;
    font-size: 62px; letter-spacing: 1px; color: var(--white);
  }
  .tier-details {
    right: 0; padding: 22px 0 0 48px;
    font-family: "Fira Sans Condensed", sans-serif; font-weight: 600;
    font-size: 42px; line-height: 60px; letter-spacing: 1.5px;
  }
  .tier-price {
    right: 0; border-radius: 48px 0 0 48px;
    display: flex; align-items: center; justify-content: flex-end; padding-right: 26px;
    font-family: "Comfortaa", sans-serif; font-weight: 700; font-size: 58px; color: var(--white);
  }

  .platinum .tier-title { top: 38px; width: 968px; height: 96px; padding-left: 66px;
    background: linear-gradient(90deg, #e33a3a, #ef6a2a 55%, #c9802f);
    text-shadow: 4px 3px 0 #f5c400, -1px -1px 0 #f5a000; }
  .platinum .tier-details { top: 148px; left: 60px; height: 158px; background: var(--red);
    color: var(--white); text-shadow: 3px 2px 0 #f7a21d; }
  .platinum .tier-price { top: 258px; width: 352px; height: 96px;
    background: linear-gradient(90deg, #d36a1f, #e2402e); }

  .gold .tier-title { top: 398px; width: 892px; height: 96px; padding-left: 96px;
    background: linear-gradient(90deg, #fff23a, #f9a825 45%, #ec3b3b);
    text-shadow: 3px 0 0 var(--red), -3px 0 0 var(--red), 0 3px 0 var(--red), 0 -3px 0 var(--red); }
  .gold .tier-details { top: 504px; left: 68px; height: 126px; padding-top: 4px; background: var(--yellow);
    color: var(--red); text-shadow: 2px 2px 0 var(--white); }
  .gold .tier-price { top: 584px; width: 348px; height: 96px; padding-right: 40px;
    background: linear-gradient(90deg, #ec4a3a, #f7941d 55%, #ffd11a); }

  .silver .tier-title { top: 694px; width: 862px; height: 98px; padding-left: 54px;
    background: linear-gradient(90deg, var(--green-dark), #2e9e44 45%, #7cc45a);
    text-shadow: 4px 3px 0 var(--red); }
  .silver .tier-details { top: 802px; left: 58px; height: 104px; padding-top: 14px; background: var(--green);
    color: var(--white); text-shadow: 3px 2px 0 var(--red); }
  .silver .tier-price { top: 878px; width: 352px; height: 76px; padding-right: 28px;
    background: linear-gradient(90deg, var(--green-dark), var(--green) 45%, #6cbd4f); }

  .express .tier-title { top: 960px; width: 860px; height: 98px; padding-left: 28px;
    background: linear-gradient(90deg, #4c4ba0, #3a86cc 45%, #abdcf6);
    text-shadow: 3px 3px 0 var(--red); }
  .express .tier-details { top: 1068px; left: 58px; height: 84px; padding-top: 8px; background: var(--blue);
    color: var(--white); text-shadow: 3px 2px 0 var(--red); }
  .express .tier-price { top: 1110px; width: 316px; height: 78px; padding-right: 30px;
    background: linear-gradient(90deg, #574b9e, #3f8fd3 50%, #b5e2f8); }
</style>
</head>
<body>
<main class="menu">
  <div class="backdrop" role="img" aria-label="Background of soap bubbles on blue water"></div>

  <section class="tier platinum">
    <h2 class="tier-title">PLATINUM WASH</h2>
    <p class="tier-details">PRE-SOAK, SOAP &amp; SCRUB , RINSE, TIRE SHINE<br>+ PLATINUM PROTECT</p>
    <p class="tier-price">$200.00</p>
  </section>

  <section class="tier gold">
    <h2 class="tier-title">GOLD WASH</h2>
    <p class="tier-details">PRE-SOAK, SOAP &amp; SCRUB , RINSE, TIRE SHINE<br>+ AQUA X POLISH</p>
    <p class="tier-price">$150.00</p>
  </section>

  <section class="tier silver">
    <h2 class="tier-title">SILVER WASH</h2>
    <p class="tier-details">PRE-SOAK, SOAP &amp; SCRUB , RINSE, TIRE SHINE</p>
    <p class="tier-price">$100.00</p>
  </section>

  <section class="tier express">
    <h2 class="tier-title">EXPRESS WASH</h2>
    <p class="tier-details">PRE-SOAK, SOAP, RINSE</p>
    <p class="tier-price">$50.00</p>
  </section>
</main>
</body>
</html>
```